Redesign Business Cards, Attached

Please read instructions carefully. If you have any questions send a message before submitting your ONE design. Please redesign attached business cards. Double sided. Use same content and descriptions. Use black, silver, crimson red and gold colors. My only issue with the attached design is the background colors. I like the layout as-is. I can provide the individual pictures on the back side later. Do not submit more than one design. One submission shall include both front and back. Do not submit front and back separately. A second project will be launched to create a matching post card after completion of this.
Industry/Entity Type
see description and attachments.
Contact Information for Business Card
Requirements
Must have
- see description and attachments.
Nice to have
Should not have

```html
<!DOCTYPE html>
<html lang="en">
<head>
<meta charset="utf-8">
<title>Helmwise Marine Training – Business Card</title>
<link href="https://fonts.googleapis.com/css2?family=Montserrat:wght@400;500;600;700&display=swap" rel="stylesheet">
<style>
  :root {
    --stage: #8f8f8f;
    --ink: #050505;
    --paper: #ffffff;
    --gold: #d1a418;
    --crimson: #d3163a;
    --sea-deep: #2c4257;
    --sea-mid: #6f8fa8;
    --sea-light: #c9d9e6;
    --band: rgba(10, 12, 16, 0.82);
  }
  * { margin: 0; padding: 0; box-sizing: border-box; }
  html, body { width: 1200px; height: 1200px; overflow: hidden; }
  body {
    background: var(--stage);
    font-family: "Montserrat", Arial, sans-serif;
    position: relative;
  }
  .card {
    position: absolute;
    left: 281px;
    width: 641px;
    height: 366px;
    border-radius: 18px;
    overflow: hidden;
  }
  .card--front { top: 195px; background: var(--paper); }
  .card--back { top: 639px; }

  .front-shape { position: absolute; inset: 0; }

  .identity { position: absolute; left: 42px; top: 58px; color: var(--paper); }
  .identity__name {
    color: var(--gold);
    font-weight: 700;
    font-size: 26px;
    letter-spacing: -0.3px;
    line-height: 1;
    white-space: nowrap;
  }
  .identity__role { font-size: 17.5px; font-weight: 500; line-height: 21px; margin-top: 4px; }
  .identity__rule { width: 42px; height: 2px; background: var(--crimson); margin-top: 14px; }

  .contact { position: absolute; left: 42px; top: 158px; list-style: none; color: var(--paper); }
  .contact__item { display: flex; align-items: center; height: 22px; font-size: 15.5px; white-space: nowrap; }
  .contact__item--phone { font-weight: 700; font-size: 16.5px; margin-bottom: 1px; }
  .contact__icon { width: 15px; height: 15px; margin-right: 11px; flex: none; }

  .badges { position: absolute; left: 42px; top: 246px; display: flex; gap: 17px; }
  .badge { width: 54px; height: 58px; }

  .brand {
    position: absolute;
    left: 400px; top: 110px;
    width: 200px; height: 160px;
    display: flex; flex-direction: column; align-items: center; justify-content: center;
    gap: 14px;
  }
  .brand__mark { width: 34px; height: 34px; border-radius: 50%; background: var(--gold); }
  .brand__name {
    color: var(--ink);
    font-weight: 700;
    font-size: 20px;
    line-height: 25px;
    text-align: center;
    text-transform: uppercase;
  }

  .back-photo {
    position: absolute; inset: 0;
    background:
      radial-gradient(ellipse 220px 170px at 480px 200px, #f2f5f8 0%, rgba(242,245,248,0) 70%),
      linear-gradient(160deg, var(--sea-mid) 0%, var(--sea-light) 45%, var(--sea-mid) 70%, var(--sea-deep) 100%);
  }
  .services { position: absolute; left: 0; top: 53px; list-style: none; }
  .services__item {
    display: flex; align-items: center;
    height: 25px; margin-bottom: 8.2px;
    width: 420px;
    padding-left: 25px;
    color: var(--paper);
    font-size: 15px;
    white-space: nowrap;
    background: linear-gradient(90deg, var(--band) 0%, var(--band) 62%, rgba(10,12,16,0) 100%);
  }
  .services__item::before {
    content: "";
    width: 7px; height: 7px; border-radius: 50%;
    background: var(--gold);
    margin-right: 7px;
    flex: none;
  }
  .services__item--long { letter-spacing: -0.4px; }
</style>
</head>
<body>

<section class="card card--front" aria-label="Business card front">
  <svg class="front-shape" viewBox="0 0 641 366" aria-hidden="true">
    <path d="M0 0 H290 C340 40 370 100 350 170 C330 230 270 280 300 330 C305 345 310 358 312 366 H0 Z" fill="var(--ink)"/>
    <path d="M343 37 C375 70 385 115 368 175 C350 230 285 260 296 310 C300 330 308 345 315 357" fill="none" stroke="var(--gold)" stroke-width="5" stroke-linecap="round"/>
  </svg>

  <div class="identity">
    <h1 class="identity__name">MARCUS B. HOLLAND</h1>
    <p class="identity__role">USCG Licensed Captain<br>Certified Instructor</p>
    <div class="identity__rule"></div>
  </div>

  <ul class="contact">
    <li class="contact__item contact__item--phone">
      <svg class="contact__icon" viewBox="0 0 16 16" aria-hidden="true"><path d="M3 1.5 L5.5 1 L7 4.5 L5.3 5.8 C6.2 7.8 7.8 9.6 10 10.7 L11.3 9 L15 10.5 L14.5 13 C14 14.5 12.5 15 11 14.5 C6 13 2.5 9 1.3 4.7 C1 3.2 1.7 2 3 1.5 Z" fill="var(--gold)"/></svg>
      Text (555) 014-2270
    </li>
    <li class="contact__item">
      <svg class="contact__icon" viewBox="0 0 16 16" aria-hidden="true"><rect x="1" y="3.5" width="14" height="9.5" fill="var(--gold)"/><path d="M1 3.5 L8 9 L15 3.5" fill="none" stroke="var(--ink)" stroke-width="1.2"/></svg>
      hello@helmwisemarine.com
    </li>
    <li class="contact__item">
      <svg class="contact__icon" viewBox="0 0 16 16" aria-hidden="true"><circle cx="8" cy="8" r="7" fill="var(--gold)"/><path d="M8 1 C5 4 5 12 8 15 M8 1 C11 4 11 12 8 15 M1 8 H15" fill="none" stroke="var(--ink)" stroke-width="1"/></svg>
      www.helmwisemarine.com
    </li>
  </ul>

  <div class="badges">
    <svg class="badge" viewBox="0 0 54 58" role="img" aria-label="Boating instructor certification badge">
      <circle cx="27" cy="27" r="25" fill="#2f78c2"/>
      <circle cx="27" cy="27" r="17" fill="var(--paper)"/>
    </svg>
    <svg class="badge" viewBox="0 0 54 58" role="img" aria-label="Veteran owned business verification badge">
      <circle cx="27" cy="27" r="25" fill="#1f3b7a"/>
      <rect x="2" y="29" width="50" height="9" fill="var(--crimson)"/>
    </svg>
  </div>

  <div class="brand">
    <span class="brand__mark" aria-hidden="true"></span>
    <p class="brand__name">Helmwise Marine<br>Training</p>
  </div>
</section>

<section class="card card--back" aria-label="Business card back">
  <div class="back-photo" role="img" aria-label="Aerial photo of a white center-console boat cruising across sparkling blue water"></div>
  <ul class="services">
    <li class="services__item">Hands-On Boat Training</li>
    <li class="services__item">Introduction to Power Boating</li>
    <li class="services__item">Precision Docking &amp; Boat Handling</li>
    <li class="services__item">Open Water Boat Handling</li>
    <li class="services__item">Inland Anchoring</li>
    <li class="services__item">Open Water Advanced Maneuvers</li>
    <li class="services__item">Coastal Navigation</li>
    <li class="services__item services__item--long">Captaining / Piloting Service for Your Outings</li>
  </ul>
</section>

</body>
</html>
```